BHP Business Cards

I need business cards for "copper glen partners llc" doublesided... logo on the back (also include logo on front)
logo attached to project... i have jpg up.. let me know if you need eps file.
Company Info:
842 East Marlow Avenue, Suite 7B
Chicago, Illinois 60617
facsimile 312-555-4186 (list fax, address, website on all cards.)
www.copperglenpartnersllc.example
Three different people on cards:
Dorian K. Patel, CPA MST
Principal
ofc 312-555-0271
mobile 312-555-0388
doriankpatel@copperglenpartnersllc.example
Harold J. Quenby, CPA MST
Principal
haroldjquenby@copperglenpartnersllc.example
mobile 708-555-0149
ofc 312-555-0271
Miles T Carver
Principal
ofc 312-555-0271
no mobile
milestcarver@copperglenpartnersllc.example
I have multiple projects listed.. see below:
Business cards for copper glen partners llc
letterhead
envelopes
Business cards for KM Holdings LLC
letterhead
envelopes
rich people
Business

```html
<!DOCTYPE html>
<html lang="en">
<head>
<meta charset="utf-8">
<title>Copper Glen Partners LLC – Business Card</title>
<link rel="stylesheet" href="https://fonts.googleapis.com/css2?family=Crimson+Text:wght@400;600&display=swap">
<style>
  :root {
    --navy: #003f74;
    --grey-band: #d5d5d5;
    --grey-soft: #f0f0f0;
    --paper: #ffffff;
    --backdrop: #6e6e6e;
    --ink: #1e1e1e;
    --serif: "Crimson Text", Georgia, serif;
  }
  * { margin: 0; padding: 0; box-sizing: border-box; }
  html, body {
    width: 1200px; height: 439px; overflow: hidden;
    background: var(--backdrop);
  }
  .stage {
    position: absolute; left: 0; top: 0;
    width: 1366px; height: 500px;
    transform: scale(0.87848);
    transform-origin: 0 0;
  }
  .card {
    position: absolute; top: 38px;
    width: 652px; height: 428px;
    background: var(--paper);
    box-shadow: 2px 3px 6px rgba(0,0,0,0.45);
    overflow: hidden;
    font-family: var(--serif);
    color: var(--navy);
  }
  .card--front { left: 20px; }
  .card--back { left: 697px; width: 650px; }
  .card__shapes { position: absolute; inset: 0; width: 100%; height: 100%; }

  .brand { position: absolute; text-align: center; }
  .brand__mark {
    display: block; margin: 0 auto;
    border-radius: 50%;
    background: var(--navy);
  }
  .brand__name {
    display: block;
    font-weight: 400;
    text-transform: uppercase;
    white-space: nowrap;
    color: var(--navy);
  }
  .card--front .brand { left: 0; right: 0; top: 172px; }
  .card--front .brand__mark { width: 92px; height: 92px; margin-bottom: 14px; }
  .card--front .brand__name { font-size: 27px; letter-spacing: 1.5px; }

  .card--back .brand { right: 22px; top: 258px; width: 240px; }
  .card--back .brand__mark { width: 44px; height: 44px; margin-bottom: 8px; }
  .card--back .brand__name { font-size: 13px; letter-spacing: 0.6px; }

  .contact-list { position: absolute; left: 62px; top: 108px; list-style: none; }
  .contact-list__item {
    position: relative; display: flex; align-items: center;
    font-size: 11.5px; line-height: 17px; color: var(--navy);
    margin-bottom: 11px;
  }
  .contact-list__icon { width: 26px; height: 26px; margin-right: 22px; flex: none; }
  .contact-list__item--address { align-items: flex-start; margin-bottom: 8px; }

  .person { position: absolute; right: 22px; top: 130px; text-align: right; }
  .person__name {
    font-size: 19px; letter-spacing: 1px; text-transform: uppercase;
    font-weight: 400; line-height: 24px;
    border-bottom: 1px solid var(--navy); padding-bottom: 1px;
  }
  .person__title { font-size: 17px; letter-spacing: 4px; line-height: 26px; margin-right: -4px; }
</style>
</head>
<body>
<main class="stage">

  <section class="card card--front" aria-label="Card front">
    <svg class="card__shapes" viewBox="0 0 652 428" preserveAspectRatio="none" aria-hidden="true">
      <polygon points="0,0 240,0 322,70 120,150 0,150" fill="var(--grey-band)"/>
      <polygon points="240,0 652,0 652,80 330,80" fill="var(--navy)"/>
      <polygon points="322,388 652,388 652,428 362,428" fill="var(--grey-band)"/>
      <polygon points="0,373 300,373 357,428 0,428" fill="var(--navy)"/>
    </svg>
    <div class="brand">
      <span class="brand__mark"></span>
      <span class="brand__name">Copper Glen Partners llc</span>
    </div>
  </section>

  <section class="card card--back" aria-label="Card back">
    <svg class="card__shapes" viewBox="0 0 650 428" preserveAspectRatio="none" aria-hidden="true">
      <rect x="0" y="25" width="650" height="370" fill="var(--grey-soft)"/>
      <polygon points="0,45 295,45 335,65 0,65" fill="var(--grey-band)"/>
      <polygon points="295,25 650,25 650,80 340,80" fill="var(--navy)"/>
      <polygon points="343,295 595,225 650,225 650,375 415,375" fill="var(--grey-band)"/>
      <polygon points="0,295 330,295 415,375 0,375" fill="var(--navy)"/>
      <rect x="22" y="45" width="615" height="353" fill="none" stroke="#ffffff" stroke-width="1" stroke-dasharray="3 3"/>
    </svg>

    <ul class="contact-list">
      <li class="contact-list__item contact-list__item--address">
        <svg class="contact-list__icon" viewBox="0 0 26 26" aria-hidden="true">
          <path d="M13 3a6 6 0 0 0-6 6c0 4.5 6 13 6 13s6-8.5 6-13a6 6 0 0 0-6-6z" fill="var(--ink)"/>
          <circle cx="13" cy="9" r="2.2" fill="var(--grey-soft)"/>
        </svg>
        <span>842 East Marlow Avenue, Suite 7B<br>Chicago, Illinois 60617</span>
      </li>
      <li class="contact-list__item">
        <svg class="contact-list__icon" viewBox="0 0 26 26" aria-hidden="true">
          <circle cx="13" cy="13" r="11" fill="none" stroke="var(--ink)" stroke-width="1.6"/>
          <path d="M9 7l2.5 0 1 3-1.6 1.2a8 8 0 0 0 3.9 3.9L16 13.5l3 1v2.5c-6 .5-10.5-4-10-10z" fill="var(--ink)"/>
        </svg>
        <span>312-555-0271</span>
      </li>
      <li class="contact-list__item">
        <svg class="contact-list__icon" viewBox="0 0 26 26" aria-hidden="true">
          <rect x="8" y="5" width="9" height="17" rx="1.5" fill="none" stroke="var(--ink)" stroke-width="1.6"/>
          <rect x="10" y="8" width="5" height="5" fill="var(--ink)"/>
          <path d="M19 8a4 4 0 0 1 0 5M21 6a7 7 0 0 1 0 9" fill="none" stroke="var(--ink)" stroke-width="1.2"/>
        </svg>
        <span>312-555-0388</span>
      </li>
      <li class="contact-list__item">
        <svg class="contact-list__icon" viewBox="0 0 26 26" aria-hidden="true">
          <rect x="2" y="7" width="22" height="13" fill="var(--ink)"/>
          <path d="M2 7l11 8 11-8" fill="none" stroke="var(--grey-soft)" stroke-width="1.4"/>
        </svg>
        <span>doriankpatel@copperglenpartnersllc.example</span>
      </li>
      <li class="contact-list__item">
        <svg class="contact-list__icon" viewBox="0 0 26 26" aria-hidden="true">
          <circle cx="13" cy="13" r="11" fill="var(--ink)"/>
          <g fill="none" stroke="var(--grey-soft)" stroke-width="1.1">
            <ellipse cx="13" cy="13" rx="4.5" ry="11"/>
            <line x1="2" y1="13" x2="24" y2="13"/>
            <line x1="13" y1="2" x2="13" y2="24"/>
            <path d="M4.5 7.5h17M4.5 18.5h17"/>
          </g>
        </svg>
        <span>www.copperglenpartnersllc.example</span>
      </li>
    </ul>

    <div class="person">
      <h1 class="person__name">Dorian K. Patel, CPA MST</h1>
      <p class="person__title">Principal</p>
    </div>

    <div class="brand">
      <span class="brand__mark"></span>
      <span class="brand__name">Copper Glen Partners llc</span>
    </div>
  </section>

</main>
</body>
</html>
```